Marvane Painting Epoxy Flyer

We need a promotional flyer for a new epoxy floor coatings division of our painting company. We do epoxy garage floor coatings and paver sealing. It needs to be based on and very similar to the attached flyer. The garage floor picture needs to look more realistic, and the before and after pavers pictures should look less shiny but still a good contrast. Include attached logo

```html
<!DOCTYPE html>
<html lang="en">
<head>
<meta charset="UTF-8">
<title>Marvane Painting – Epoxy Flyer</title>
<link href="https://fonts.googleapis.com/css2?family=Bebas+Neue&family=Montserrat:ital,wght@0,500;0,600;0,700;0,800;1,400;1,500&display=swap" rel="stylesheet">
<style>
  :root {
    --green: #2f9a47;
    --blue: #274796;
    --ink: #1c1c1e;
    --paper: #ffffff;
    --backdrop: #e4e4e6;
    --rule: #d9dbe0;
    --label-band: rgba(70, 70, 72, 0.72);
  }
  * { margin: 0; padding: 0; box-sizing: border-box; }
  html, body { width: 1200px; height: 2250px; overflow: hidden; background: var(--backdrop); }
  body { position: relative; font-family: "Montserrat", sans-serif; color: var(--ink); }

  .flyer {
    position: absolute; left: 55px; top: 353px;
    width: 778px; height: 1102px;
    background: var(--paper);
    transform: scale(1.4); transform-origin: top left;
    overflow: hidden;
  }
  .abs { position: absolute; }

  /* Brand */
  .brand { left: 42px; top: 84px; width: 240px; display: flex; align-items: center; gap: 10px; }
  .brand-dot { width: 28px; height: 28px; border-radius: 50%; background: var(--green); flex: none; }
  .brand-name { font-family: "Montserrat", sans-serif; font-weight: 700; font-size: 17px; color: var(--ink); letter-spacing: 0.3px; line-height: 1.15; white-space: nowrap; }

  /* Headline */
  .headline { left: 302px; top: 36px; font-family: "Bebas Neue", sans-serif; font-weight: 400; font-size: 57px; line-height: 50px; color: var(--ink); letter-spacing: 1.6px; }
  .headline .accent { color: var(--blue); display: block; }
  .subhead { left: 302px; top: 140px; font-style: italic; font-weight: 400; font-size: 30px; color: var(--ink); }

  /* Photo grid */
  .photo { overflow: hidden; }
  .photo-label {
    position: absolute; left: 0; right: 0; bottom: 0; height: 33px;
    background: var(--label-band); color: #fff; text-align: center;
    font-family: "Bebas Neue", sans-serif; font-size: 27px; line-height: 36px;
  }
  .garage-before { left: 29px; top: 196px; width: 256px; height: 308px; background: linear-gradient(160deg, #a7b0b5 0%, #8c969c 45%, #717b80 100%); }
  .garage-after { left: 293px; top: 196px; width: 248px; height: 308px; background: linear-gradient(180deg, #a5a8ae 0%, #b9bcc1 60%, #aeb1b6 100%); }
  .paver-before { left: 548px; top: 196px; width: 201px; height: 150px; background: linear-gradient(160deg, #9d9196 0%, #857b80 55%, #6f686b 100%); }
  .paver-after { left: 548px; top: 353px; width: 201px; height: 151px; background: linear-gradient(160deg, #c1705a 0%, #a9584a 55%, #8f4a40 100%); }

  /* Services box */
  .services { left: 55px; top: 528px; width: 668px; height: 219px; border: 2px solid var(--blue); border-top-color: var(--green); }
  .services::before { content: ""; position: absolute; left: -2px; top: -2px; width: 2px; height: 100px; background: var(--green); }
  .services::after { content: ""; position: absolute; right: -2px; top: -2px; width: 2px; height: 100px; background: var(--green); }
  .service { position: absolute; top: 18px; width: 306px; }
  .service.epoxy { left: 19px; }
  .service.pavers { left: 339px; }
  .service-title { height: 36px; color: #fff; font-family: "Bebas Neue", sans-serif; font-weight: 400; font-size: 27px; line-height: 38px; padding-left: 16px; }
  .epoxy .service-title { background: var(--green); }
  .pavers .service-title { background: var(--blue); }
  .service-list { list-style: none; padding-top: 4px; }
  .service-list li { display: flex; align-items: center; gap: 12px; height: 36px; padding-left: 6px; font-style: italic; font-size: 14.5px; border-bottom: 1px solid var(--rule); }
  .service-list li:last-child { border-bottom: none; }
  .pavers .service-list li { font-size: 14px; padding-left: 0; }
  .tick { width: 17px; height: 17px; flex: none; }

  /* Trust band */
  .trust-band { left: 0; top: 793px; width: 778px; height: 108px; background: var(--blue); }
  .tagline-bar { left: 55px; top: 772px; width: 668px; height: 41px; background: var(--green); color: #fff; text-align: center; font-weight: 700; font-size: 16.5px; line-height: 41px; letter-spacing: 0.2px; }
  .trust { position: absolute; top: 829px; display: flex; align-items: center; gap: 14px; color: #fff; font-weight: 600; font-size: 16.5px; line-height: 21px; }
  .trust-icon { width: 52px; height: 52px; border-radius: 50%; background: #fff; display: flex; align-items: center; justify-content: center; flex: none; }
  .trust-icon svg { width: 30px; height: 30px; }
  .trust.licensed { left: 76px; }
  .trust.family { left: 260px; }
  .trust.area { left: 478px; }
  .divider { position: absolute; top: 832px; width: 1px; height: 50px; background: rgba(255,255,255,0.55); }

  /* Call to action */
  .cta-heading { left: 76px; top: 922px; width: 626px; display: flex; align-items: center; gap: 14px; font-family: "Bebas Neue", sans-serif; font-size: 40px; color: var(--blue); white-space: nowrap; }
  .cta-heading .rule { flex: 1; height: 2px; background: var(--blue); }
  .cta-heading .rule.green { background: var(--green); }
  .cta-heading em { font-style: normal; color: var(--green); }
  .phone { left: 76px; top: 958px; display: flex; align-items: center; gap: 12px; white-space: nowrap; }
  .phone svg { width: 46px; height: 62px; flex: none; }
  .phone-number { font-weight: 800; font-size: 84px; letter-spacing: -1px; color: var(--ink); line-height: 90px; }
  .cta-note { left: 0; width: 778px; top: 1046px; text-align: center; font-style: italic; font-size: 23px; }
</style>
</head>
<body>
<main class="flyer">
  <div class="abs brand">
    <span class="brand-dot"></span>
    <span class="brand-name">MARVANE PAINTING</span>
  </div>

  <h1 class="abs headline">Upgrade your garage<span class="accent">&amp; Driveway</span></h1>
  <p class="abs subhead">From worn-out to like new</p>

  <div class="abs photo garage-before" role="img" aria-label="Worn grey concrete garage floor before coating"><span class="photo-label">Before</span></div>
  <div class="abs photo garage-after" role="img" aria-label="Speckled epoxy flake garage floor after coating"><span class="photo-label">After</span></div>
  <div class="abs photo paver-before" role="img" aria-label="Faded brick pavers before sealing"><span class="photo-label">Before</span></div>
  <div class="abs photo paver-after" role="img" aria-label="Restored red brick pavers after sealing"><span class="photo-label">After</span></div>

  <section class="abs services">
    <div class="service epoxy">
      <h2 class="service-title">Epoxy Floor Coatings</h2>
      <ul class="service-list">
        <li><svg class="tick" viewBox="0 0 20 20"><circle cx="10" cy="10" r="10" fill="#2f9a47"/><path d="M5.5 10.3l3 3 6-6" stroke="#fff" stroke-width="2.2" fill="none"/></svg>Durable, long-lasting finish</li>
        <li><svg class="tick" viewBox="0 0 20 20"><circle cx="10" cy="10" r="10" fill="#2f9a47"/><path d="M5.5 10.3l3 3 6-6" stroke="#fff" stroke-width="2.2" fill="none"/></svg>Protects from sun fading</li>
        <li><svg class="tick" viewBox="0 0 20 20"><circle cx="10" cy="10" r="10" fill="#2f9a47"/><path d="M5.5 10.3l3 3 6-6" stroke="#fff" stroke-width="2.2" fill="none"/></svg>Helps prevent weeds &amp; sand loss</li>
        <li><svg class="tick" viewBox="0 0 20 20"><circle cx="10" cy="10" r="10" fill="#2f9a47"/><path d="M5.5 10.3l3 3 6-6" stroke="#fff" stroke-width="2.2" fill="none"/></svg>Easier to clean &amp; maintain</li>
      </ul>
    </div>
    <div class="service pavers">
      <h2 class="service-title">Paver Sealing</h2>
      <ul class="service-list">
        <li><svg class="tick" viewBox="0 0 20 20"><circle cx="10" cy="10" r="10" fill="#274796"/><path d="M5.5 10.3l3 3 6-6" stroke="#fff" stroke-width="2.2" fill="none"/></svg>Restores color &amp; enhances appearance</li>
        <li><svg class="tick" viewBox="0 0 20 20"><circle cx="10" cy="10" r="10" fill="#274796"/><path d="M5.5 10.3l3 3 6-6" stroke="#fff" stroke-width="2.2" fill="none"/></svg>Protects from sun fading</li>
        <li><svg class="tick" viewBox="0 0 20 20"><circle cx="10" cy="10" r="10" fill="#274796"/><path d="M5.5 10.3l3 3 6-6" stroke="#fff" stroke-width="2.2" fill="none"/></svg>Helps prevent weeds &amp; sand loss</li>
        <li><svg class="tick" viewBox="0 0 20 20"><circle cx="10" cy="10" r="10" fill="#274796"/><path d="M5.5 10.3l3 3 6-6" stroke="#fff" stroke-width="2.2" fill="none"/></svg>Easier to clean &amp; maintain</li>
      </ul>
    </div>
  </section>

  <div class="abs trust-band"></div>
  <div class="abs tagline-bar">PRACTICAL UPGRADES THAT PROTECT AND IMPROVE YOUR HOME</div>

  <div class="trust licensed">
    <span class="trust-icon"><svg viewBox="0 0 30 30"><path d="M15 3l10 4v7c0 7-4.5 11-10 13C9.5 25 5 21 5 14V7z" fill="none" stroke="#274796" stroke-width="2.4"/><path d="M10.5 15l3 3 6-6" fill="none" stroke="#274796" stroke-width="2.4"/></svg></span>
    <span>Licensed &amp;<br>Insured</span>
  </div>
  <span class="divider" style="left:246px"></span>
  <div class="trust family">
    <span class="trust-icon"><svg viewBox="0 0 30 30"><path d="M4 21c3-2 6-2 9-1l5 1c1.5.3 1.5 2 0 2h-5m-9 2l5-1 8 1 8-5" fill="none" stroke="#274796" stroke-width="2.2" stroke-linecap="round"/><path d="M9 6l1 2 2 .3-1.5 1.4.4 2.1L9 10.8 7.1 11.8l.4-2.1L6 8.3 8 8zM15 4l1 2 2 .3-1.5 1.4.4 2.1L15 8.8l-1.9 1 .4-2.1L12 6.3l2-.3zM21 6l1 2 2 .3-1.5 1.4.4 2.1-1.9-1-1.9 1 .4-2.1L18 8.3l2-.3z" fill="#274796"/></svg></span>
    <span>Family-Owned<br>Local Business</span>
  </div>
  <span class="divider" style="left:463px"></span>
  <div class="trust area">
    <span class="trust-icon"><svg viewBox="0 0 30 30"><path d="M15 3c-5 0-8.5 3.7-8.5 8.5C6.5 18 15 27 15 27s8.5-9 8.5-15.5C23.5 6.7 20 3 15 3z" fill="#274796"/><circle cx="15" cy="11.5" r="3.6" fill="#fff"/></svg></span>
    <span>Serving Prescott &amp;<br>Surrounding Areas</span>
  </div>

  <div class="abs cta-heading"><span class="rule"></span><span>Call for a <em>Free Estimate</em></span><span class="rule green"></span></div>
  <div class="abs phone">
    <svg viewBox="0 0 46 62"><path d="M9 4c3-2 6-1 7 2l4 10c1 3 0 5-2 6l-4 2c1 8 5 16 11 21l4-2c2-1 4-1 6 1l6 8c2 2 1 5-1 7l-4 2C22 62 3 36 4 12c0-3 2-6 5-8z" fill="#2f9a47"/></svg>
    <span class="phone-number">928-555-0147</span>
  </div>
  <p class="abs cta-note">Fast, professional service you can trust</p>
</main>
</body>
</html>
```